make it look old timey and motherly but mordern...bath soak with cooling vapors. tall pine hush

need a bath soak label...cooling vapors. will be in a pouch like below. dont pay attention to the design, just attatching so you know the kind of pouch itll be in. need something trusty, minimal and clean...its called tall pine hush bath soak the best bath yull ever take.... for sore muscles, cooling vapors, smells good...made with menthol lemon and eucalyptus...give me something good.

Target Market(s)

make it look old timey and motherly but mordern

Font styles to use
Serif
Sans Serif

Colors
0054AA
0677BA
7BADD7
CADEEF
E8F1F8
0094D4
00A9DD
6FCCEA
C7EBF8
E9F6FB
FFF300
FFF600
FEFA6F
FFFEC7
FFFEE8
FFC000
F8CF3A
FAE287
FDF2CF
FEFAEE
E54698
E96AAD
F1A4CE
F9D9EA
FCEFF6
6B429C
8869AF
B7A5CE
E3DAEB
F3F0F8

```html
<!DOCTYPE html>
<html lang="en">
<head>
<meta charset="utf-8">
<title>Tall Pine Hush Bath Soak</title>
<link rel="stylesheet" href="https://fonts.googleapis.com/css2?family=Roboto+Slab:wght@400;700;800&family=Montserrat:wght@400;600;700&display=swap">
<style>
  :root {
    --violet-deep: #6a68a6;
    --violet-mid: #9c99cf;
    --lavender: #c2bfe2;
    --mist: #e4e3ee;
    --white-soft: #f3f3f5;
    --ink-violet: #6f6cae;
    --text-light: #f4f3f8;
    --chip-bg: rgba(255,255,255,0.35);
  }
  * { margin: 0; padding: 0; box-sizing: border-box; }
  html, body { width: 953px; height: 1200px; overflow: hidden; background: #fafafa; }
  .label {
    position: relative;
    width: 953px;
    height: 1200px;
    overflow: hidden;
    background:
      radial-gradient(ellipse 60% 30% at 30% 40%, rgba(255,255,255,0.18), transparent 70%),
      radial-gradient(ellipse 50% 25% at 75% 30%, rgba(255,255,255,0.12), transparent 70%),
      linear-gradient(180deg, var(--violet-deep) 0%, #7b79b7 22%, var(--violet-mid) 42%, var(--lavender) 60%, var(--mist) 78%, var(--white-soft) 100%);
    font-family: 'Montserrat', sans-serif;
    color: var(--text-light);
  }
  .brand-seal {
    position: absolute;
    left: 396px; top: 146px;
    width: 160px; height: 160px;
    border-radius: 50%;
    background: var(--text-light);
  }
  .title-block {
    position: absolute;
    top: 322px; left: 0; width: 100%;
    text-align: center;
    font-family: 'Roboto Slab', serif;
  }
  .brand-name { font-size: 49px; font-weight: 700; line-height: 1; letter-spacing: -0.5px; text-transform: uppercase; }
  .product-name { font-size: 92px; font-weight: 800; line-height: 0.95; letter-spacing: -1px; margin-top: 2px; }
  .tagline { font-size: 27px; font-weight: 800; line-height: 1; margin-top: 12px; }
  .benefit {
    position: absolute; top: 519px; width: 100%;
    text-align: center; font-size: 21px; font-weight: 600; letter-spacing: 0.3px;
  }
  .crystal-art {
    position: absolute; left: 408px; top: 576px;
    width: 140px; height: 148px;
    border-radius: 10px;
    background: radial-gradient(circle at 50% 55%, rgba(255,255,255,0.55), rgba(255,255,255,0.12) 70%);
  }
  .claims {
    position: absolute; top: 762px; width: 100%;
    text-align: center; font-size: 21px; font-weight: 700; line-height: 1.25;
  }
  .ingredients { position: absolute; left: 94px; top: 938px; }
  .ingredient {
    display: flex; align-items: center;
    height: 60px; margin-bottom: 13px;
    padding: 0 14px 0 10px;
    border-radius: 6px;
    background: var(--chip-bg);
    color: var(--ink-violet);
  }
  .ingredient.menthol { width: 219px; }
  .ingredient.lemon { width: 220px; }
  .ingredient.eucalyptus { width: 252px; }
  .ingredient-icon {
    width: 44px; height: 40px; margin-right: 10px; flex: none;
    border-radius: 50%;
    background: rgba(111,108,174,0.22);
  }
  .ingredient-name { font-size: 23px; font-weight: 700; line-height: 1; }
  .ingredient-note { font-size: 17px; font-weight: 400; line-height: 1.2; opacity: 0.9; }
  .net-weight {
    position: absolute; left: 712px; top: 1080px;
    font-family: 'Roboto Slab', serif; font-size: 24px; line-height: 1.2;
    color: var(--ink-violet);
  }
</style>
</head>
<body>
  <main class="label">
    <div class="brand-seal" aria-hidden="true"></div>

    <header class="title-block">
      <p class="brand-name">Tall Pine Hush</p>
      <h1 class="product-name">BATH SOAK</h1>
      <p class="tagline">THE BEST BATH YULL EVER TAKE</p>
    </header>

    <p class="benefit">CALM + HYDRATE</p>

    <div class="crystal-art" role="img" aria-label="Line illustration of bath crystals with rising vapor and a snowflake"></div>

    <p class="claims">REFRESH+RELIEVE+REJOICE<br>AROMA-COOL SOAP</p>

    <ul class="ingredients" style="list-style:none">
      <li class="ingredient menthol">
        <span class="ingredient-icon" role="img" aria-label="Mint leaf icon"></span>
        <span><span class="ingredient-name">MENTHOL</span><br><span class="ingredient-note">Cooling</span></span>
      </li>
      <li class="ingredient lemon">
        <span class="ingredient-icon" role="img" aria-label="Lemon slice icon"></span>
        <span><span class="ingredient-name">LEMON</span><br><span class="ingredient-note">Moisturizing</span></span>
      </li>
      <li class="ingredient eucalyptus">
        <span class="ingredient-icon" role="img" aria-label="Eucalyptus leaf icon"></span>
        <span><span class="ingredient-name">EUCALYPTUS</span><br><span class="ingredient-note">Anti Bacterial</span></span>
      </li>
    </ul>

    <p class="net-weight">Net Weight :<br>15 ounces<br>(425 grams)</p>
  </main>
</body>
</html>
```